Coin Donation Box Home version ELEGANT

The idea is to hand out/mail a coin donation box that can be folded/assembled by the receiving party. It should be attractive so people would put it on their desk/night stand to collect change, with instructions on the bottom how to then bring it in for donation to charitable organizations. Similar to Corvana Halloween idea where boxes are shipped to schools, assembled by kids, then carried around for donations. This one should be different - it stays at the person's house until its filled, so should be more durable/attractive. Maybe reusable too? What material - cardboard, plastic, any other new cool materials? Will need logos/instructions. Classy and elegant to encourage prominent display - like a design piece rather than bright in-store ones. maybe the top cover, when opened, has the information and instructions. maybe the size of the rectangular Tessory box?

Target Market(s)

families, offices

Industry/Entity Type

Charity

Font styles to use
Serif

Colors

Designer to choose colors to be used in the design.

Requirements
Must have
• Easy to self-assemble, inexpensive to mass produce, durable to hold heavy coins.
Nice to have
• Elegant - something a person would like to display on their desk or night stand. People use jars at home to dump change our of their pockets in the evening. This can be an alternative, and used for charity donations.

```html
<!DOCTYPE html>
<html lang="en">
<head>
<meta charset="utf-8">
<title>Young Hearts Give – Coin Donation Box</title>
<link rel="stylesheet" href="https://fonts.googleapis.com/css2?family=Open+Sans:wght@700&family=Krona+One&display=swap">
<style>
  :root {
    --backdrop: #6d6e71;
    --shadow: #646567;
    --panel-pink: #f5c4dc;
    --stripe-pink: #efb3d0;
    --band-pink: #f7d0e4;
    --slot-pink: #ec6aa9;
    --slot-edge: #c96a9a;
    --text-white: #ffffff;
    --art-white: #fdf4f8;
    --art-yellow: #f9d48a;
    --art-purple: #b7a3d6;
    --art-pink: #ee9cc5;
    --art-blue: #9fd8ef;
  }
  html, body {
    margin: 0;
    padding: 0;
    width: 1200px;
    height: 1199px;
    overflow: hidden;
    background: var(--backdrop);
  }
  .canvas {
    position: relative;
    width: 1200px;
    height: 1199px;
    background: var(--backdrop);
  }
  .box-shadow {
    position: absolute;
    left: 94px;
    top: 1061px;
    width: 1011px;
    height: 110px;
    background: linear-gradient(to bottom, var(--shadow), var(--backdrop));
  }
  .box-face {
    position: absolute;
    left: 94px;
    top: 142px;
    width: 1011px;
    height: 919px;
    background:
      repeating-linear-gradient(to bottom,
        transparent 0 22px,
        var(--stripe-pink) 22px 25px),
      var(--panel-pink);
  }
  .title {
    position: absolute;
    left: 0;
    right: 0;
    top: 20px;
    margin: 0;
    text-align: center;
    font-family: "Open Sans", sans-serif;
    font-weight: 700;
    font-size: 62px;
    line-height: 1;
    letter-spacing: -1px;
    white-space: nowrap;
    color: var(--text-white);
  }
  .handle-cutout {
    position: absolute;
    left: 212px;
    top: 113px;
    width: 588px;
    height: 172px;
    border-radius: 86px;
    background: var(--backdrop);
  }
  .coin-band {
    position: absolute;
    left: 0;
    top: 353px;
    width: 100%;
    height: 137px;
    background: var(--band-pink);
  }
  .band-label {
    position: absolute;
    left: 0;
    right: 0;
    margin: 0;
    text-align: center;
    font-family: "Krona One", sans-serif;
    color: var(--text-white);
    line-height: 1;
    white-space: nowrap;
  }
  .band-label--collect {
    top: 12px;
    font-size: 25px;
    letter-spacing: 2px;
    transform: scaleX(1.3);
  }
  .band-label--thanks {
    top: 86px;
    font-size: 35px;
    letter-spacing: 3px;
  }
  .coin-slot {
    position: absolute;
    left: 390px;
    top: 58px;
    width: 231px;
    height: 20px;
    border-radius: 10px;
    background: var(--slot-pink);
    border-top: 4px solid var(--slot-edge);
    box-sizing: border-box;
  }
  .donate-art {
    position: absolute;
    left: 66px;
    top: 527px;
    width: 878px;
    height: 354px;
    background:
      radial-gradient(ellipse 22% 40% at 20% 35%, var(--art-purple), transparent 70%),
      radial-gradient(ellipse 18% 30% at 50% 15%, var(--art-yellow), transparent 70%),
      radial-gradient(ellipse 20% 40% at 58% 55%, var(--art-yellow), transparent 70%),
      radial-gradient(ellipse 18% 35% at 78% 70%, var(--art-blue), transparent 70%),
      radial-gradient(ellipse 18% 45% at 90% 45%, var(--art-pink), transparent 70%),
      linear-gradient(to bottom, transparent 0 25%, var(--art-white) 60%, var(--art-white) 92%, transparent 100%);
  }
</style>
</head>
<body>
  <main class="canvas">
    <div class="box-shadow"></div>
    <section class="box-face">
      <h1 class="title">Young Hearts Give</h1>
      <div class="handle-cutout"></div>
      <div class="coin-band">
        <p class="band-label band-label--collect">Collect Change Here</p>
        <div class="coin-slot"></div>
        <p class="band-label band-label--thanks">Thank You!</p>
      </div>
      <div class="donate-art" role="img" aria-label="Illustration of children and young people sitting and standing on large white letters spelling DONATE, with laptops, a coin jar, a gold dollar coin above a cloud and ladder, a payment card, gift boxes, a flower and small pink hearts"></div>
    </section>
  </main>
</body>
</html>
```